Modern Irish Pub. We need to find "our look" for new bar.

We have a logo, color scheme and feel of what we want but we need someone to work with to create flyer designs, menu, website and social content.

Young vibrant mixed with traditional Irish. Think neon & sexy mixed with wood and traditional Irish.

Looking for examples of social media posts and flyers. We can then hire for more work! We need to find “our look”.

Target Market(s)

21-40 year olds

Industry/Entity Type

Bar and Restaurant.

Colors
EB3D1F
EC4F4E
F09395
F8D3D4
FCEDEE

Requirements
Must have
• Our logo.
Nice to have
• Young mixed with traditional. Sexy l, vibrant and fun.
Should not have
• Cartoon like child like look and feel.

```html
<!DOCTYPE html>
<html lang="en">
<head>
<meta charset="utf-8">
<title>VelVette Cocktail Bar</title>
<link href="https://fonts.googleapis.com/css2?family=Italiana&family=Gilda+Display&family=Oswald:wght@600&display=swap" rel="stylesheet">
<style>
  :root {
    --ink: #0d0a0a;
    --red: #e5101d;
    --gold: #f3c433;
    --white: #ffffff;
    --rule: #8a8380;
  }
  * { margin: 0; padding: 0; box-sizing: border-box; }
  html, body { width: 927px; height: 1200px; overflow: hidden; background: var(--ink); }
  .flyer { position: relative; width: 927px; height: 1200px; overflow: hidden; background: var(--ink); }
  .bar-backdrop {
    position: absolute; inset: 0;
    background: linear-gradient(180deg, #1c1615 0%, #241c1a 40%, #130f0e 65%, #0a0808 100%);
  }
  .cocktail-photo {
    position: absolute; left: 470px; top: 615px; width: 390px; height: 570px;
    background: radial-gradient(ellipse at 55% 40%, rgba(205,45,70,0.55) 0%, rgba(120,25,40,0.3) 50%, rgba(13,10,10,0) 80%);
  }
  .pub-mark {
    position: absolute; left: 353px; top: 80px; width: 214px; height: 214px;
    border: 3px solid var(--red); border-radius: 50%;
  }
  .pub-name {
    position: absolute; top: 128px; left: 0; width: 100%; text-align: center;
    font-family: "Oswald", sans-serif; font-weight: 600; font-size: 50px; line-height: 58px;
    letter-spacing: 1px; color: var(--white);
  }
  .bar-title {
    position: absolute; top: 318px; left: 0; width: 100%; text-align: center;
    font-family: "Italiana", serif; font-weight: 400; font-size: 176px; line-height: 1; color: var(--red);
  }
  .bar-subtitle {
    position: absolute; top: 512px; left: 0; width: 100%; text-align: center;
    font-family: "Italiana", serif; font-size: 62px; color: var(--white); letter-spacing: 1px;
  }
  .info { position: absolute; left: 49px; font-family: "Gilda Display", serif; }
  .open-label { top: 707px; font-size: 36px; color: var(--gold); }
  .open-hours { top: 752px; font-size: 47px; color: var(--white); }
  .divider { position: absolute; left: 49px; top: 824px; width: 451px; height: 1px; background: var(--rule); }
  .address { top: 850px; font-size: 37px; line-height: 46px; color: var(--white); }
  .challenge {
    position: absolute; left: 49px; top: 1018px;
    font-family: "Italiana", serif; font-size: 54px; line-height: 56px; color: var(--gold);
  }
  .glass-icon { position: absolute; left: 329px; top: 1030px; width: 72px; height: 86px; }
  .schedule {
    position: absolute; left: 409px; top: 1027px;
    font-family: "Gilda Display", serif; font-size: 24px; line-height: 27px; color: var(--white);
  }
</style>
</head>
<body>
<main class="flyer">
  <div class="bar-backdrop" role="img" aria-label="Dimly lit bar shelves with blurred bottles"></div>
  <div class="cocktail-photo" role="img" aria-label="Photo of a pink strawberry martini with strawberries and red currants"></div>

  <div class="pub-mark"></div>
  <p class="pub-name">CRIMSON<br>CLOVER</p>

  <h1 class="bar-title">VelVette</h1>
  <p class="bar-subtitle">COCKTAIL BAR</p>

  <p class="info open-label">OPEN FROM</p>
  <p class="info open-hours">6PM TO 2AM</p>
  <div class="divider"></div>
  <p class="info address">218 HARBOR LANE ST.<br>PORT ALDEN, CA 94012</p>

  <p class="challenge">MIXOLOGY<br>CHALLENGE</p>
  <svg class="glass-icon" viewBox="0 0 72 86" aria-hidden="true">
    <path d="M0 22 H60 L34 48 V74 H48 V84 H18 V74 H28 V48 Z" fill="var(--red)"/>
    <circle cx="54" cy="16" r="13" fill="none" stroke="var(--red)" stroke-width="6"/>
  </svg>
  <p class="schedule">EVERY<br>TUESDAY<br>NIGHT</p>
</main>
</body>
</html>
```